Breakfast Briefings / Lunch & Learn

I would like to have a double sided flyer size 8x10 to display the breakfast briefing on one side and Lunch & Learn on the other side.

Header on each side to say
2018 Calendar Breakfast Briefing (on the breakfast side)
2018 Calendar Lunch & Learn (on the lunch side)

I have attached a copy of the files we would like to use.

Learn

```html
<!DOCTYPE html>
<html lang="en">
<head>
<meta charset="utf-8">
<title>2018 Calendar – Lunch &amp; Learn</title>
<link rel="stylesheet" href="https://fonts.googleapis.com/css2?family=Mulish:wght@300;600;700;800&display=swap">
<style>
  :root {
    --band-blue: #1b79cf;
    --title-cyan: #6ff5e8;
    --white: #ffffff;
    --month-blue: #1a78cf;
    --topic-grey: #566669;
    --divider: #9aa5a7;
    --accent-orange: #f04a14;
    --brand-grey: #54666b;
    --bg-light: #fbfcfc;
    --bg-edge: #dbe3e3;
  }
  * { margin: 0; padding: 0; box-sizing: border-box; }
  html, body { width: 960px; height: 1200px; overflow: hidden; }
  body {
    font-family: "Mulish", "Century Gothic", sans-serif;
    background: var(--bg-edge);
  }
  .flyer {
    position: relative;
    width: 960px;
    height: 1200px;
    background: radial-gradient(ellipse 60% 55% at 50% 52%, var(--bg-light) 0%, #eef2f2 55%, var(--bg-edge) 100%);
    overflow: hidden;
  }
  .header-band {
    position: absolute;
    top: 32px; left: 0;
    width: 960px; height: 232px;
    background: var(--band-blue);
  }
  .header-title {
    position: absolute;
    top: 8px; left: 0;
    width: 960px;
    text-align: center;
    white-space: nowrap;
    font-weight: 700;
    font-size: 90px;
    line-height: 1;
    letter-spacing: 1px;
    color: var(--title-cyan);
  }
  .header-rule {
    position: absolute;
    top: 123px; left: 78px;
    width: 804px; height: 4px;
    background: var(--title-cyan);
  }
  .header-subtitle {
    position: absolute;
    top: 134px; left: 0;
    width: 960px;
    text-align: center;
    white-space: nowrap;
    font-weight: 800;
    font-size: 84px;
    line-height: 1;
    color: var(--white);
  }
  .schedule {
    position: absolute;
    top: 276px; left: 94px;
    width: 823px;
    list-style: none;
  }
  .session {
    display: flex;
    align-items: center;
    height: 64px;
    border-bottom: 1px dashed var(--divider);
    font-size: 26px;
    font-weight: 600;
    white-space: nowrap;
  }
  .session:last-child { border-bottom: none; }
  .session-month {
    width: 159px;
    text-align: right;
    color: var(--month-blue);
  }
  .session-topic {
    margin-left: 44px;
    color: var(--topic-grey);
  }
  .session-topic sup { font-size: 14px; }
  .tagline {
    position: absolute;
    top: 938px; left: 0;
    width: 960px;
    text-align: center;
    font-weight: 300;
    font-size: 44px;
    letter-spacing: 1px;
    color: var(--accent-orange);
  }
  .brand {
    position: absolute;
    top: 1108px; left: 0;
    width: 960px;
    display: flex;
    justify-content: center;
    align-items: center;
    gap: 14px;
  }
  .brand-mark {
    width: 22px; height: 22px;
    background: var(--brand-grey);
  }
  .brand-name {
    font-weight: 600;
    font-size: 46px;
    letter-spacing: 4px;
    color: var(--brand-grey);
  }
</style>
</head>
<body>
  <main class="flyer">
    <header class="header-band">
      <h1 class="header-title">2018 CALENDAR</h1>
      <div class="header-rule"></div>
      <h2 class="header-subtitle">Lunch &amp; Learn</h2>
    </header>

    <ul class="schedule">
      <li class="session"><span class="session-month">March</span><span class="session-topic">Mindfulness</span></li>
      <li class="session"><span class="session-month">April</span><span class="session-topic">Nutrition and Lifestyle Coaching</span></li>
      <li class="session"><span class="session-month">May</span><span class="session-topic">What is Neuromodulation</span></li>
      <li class="session"><span class="session-month">June</span><span class="session-topic">Achieve Your Goals</span></li>
      <li class="session"><span class="session-month">July</span><span class="session-topic">Changing Your Life with Positive Thinking</span></li>
      <li class="session"><span class="session-month">August</span><span class="session-topic">What is Clean Eating and How Do I get Started</span></li>
      <li class="session"><span class="session-month">September</span><span class="session-topic">Budgeting 101 Financial Weliness</span></li>
      <li class="session"><span class="session-month">October</span><span class="session-topic">Busted Nutrition Myths</span></li>
      <li class="session"><span class="session-month">November</span><span class="session-topic">Time Management : No time like present</span></li>
      <li class="session"><span class="session-month">December</span><span class="session-topic">1<sup>st</sup> Time Home Buyers</span></li>
    </ul>

    <p class="tagline">LIFE - LONG - LEARN</p>

    <div class="brand">
      <span class="brand-mark"></span>
      <span class="brand-name">corvana</span>
    </div>
  </main>
</body>
</html>
```